IT Services

We come to you
Only $49/hr
No contract, no monthly fee
Software engineer on staff
remote assistance or visit in your office

On the back of the card I want to list services.

- Server setup
- Network troubleshooting
- Printer setup
- Secure backup setup
- Software installation
- Wireless network setup
- Wired network setup
- Disaster recovery
- Website management
- Any other technology related support
- Email setup
- HIPAA compliance review and setup
Updates

the URL is: BYTEHARBOR.ZONE please use it on the card

On the card we need to mention "Connect remotely to address your IT issues" if there is enough room as well as "we go to you"

Industry/Entity Type

Printer

Contact Information for Business Card

I want a busoiness card to offer my services to doctor offices, it can be dentists, Otamatry, and other professions. I provide the following service. My plan is to go to their office and drop off my card. I don't want them to forget about it that is why I am paying for the design. I like hand writing design formats.

```html
<!DOCTYPE html>
<html lang="en">
<head>
<meta charset="utf-8">
<title>ByteHarbor.Zone business card</title>
<link rel="stylesheet" href="https://fonts.googleapis.com/css2?family=Lato:wght@400;700&display=swap">
<style>
  :root {
    --navy: #1c2a78;
    --card-white: #ffffff;
    --page: #e9e7e2;
    --ink-light: #ffffff;
  }
  * { box-sizing: border-box; margin: 0; padding: 0; }
  html, body {
    width: 1200px;
    height: 900px;
    overflow: hidden;
    background: var(--page);
    font-family: "Lato", sans-serif;
  }
  .canvas {
    position: relative;
    width: 1200px;
    height: 900px;
  }
  .card {
    position: absolute;
    left: 320px;
    width: 560px;
    height: 320px;
    box-shadow: 0 10px 24px rgba(0, 0, 0, 0.25);
    overflow: hidden;
  }

  /* Front */
  .card-front {
    top: 95px;
    background: var(--card-white);
    color: var(--navy);
    text-align: center;
  }
  .front-bar {
    position: absolute;
    width: 34px;
    background: var(--navy);
  }
  .front-bar-left { left: 0; top: 100px; height: 200px; }
  .front-bar-right { right: 0; top: 18px; height: 150px; }
  .brand-name {
    margin-top: 52px;
    font-size: 34px;
    font-weight: 400;
    letter-spacing: 1px;
  }
  .rule {
    width: 240px;
    height: 2px;
    margin: 4px auto 3px;
    background: var(--navy);
  }
  .contact-name, .contact-phone {
    font-size: 17px;
    letter-spacing: 1px;
    line-height: 1.2;
  }
  .offer-list {
    list-style: none;
    margin-top: 14px;
    font-size: 12.5px;
    letter-spacing: 0.6px;
    line-height: 1.25;
  }

  /* Back */
  .card-back {
    top: 485px;
    background: var(--navy);
    color: var(--ink-light);
  }
  .service-list {
    position: absolute;
    left: 40px;
    top: 40px;
    list-style: none;
    font-size: 15px;
    letter-spacing: 0.8px;
    line-height: 1.27;
  }
  .service-list li::before {
    content: "\27A4";
    font-size: 11px;
    margin-right: 7px;
  }
  .service-extra {
    position: absolute;
    left: 330px;
    top: 99px;
    font-size: 15px;
    letter-spacing: 0.8px;
  }
  .back-brand {
    position: absolute;
    right: 30px;
    bottom: 34px;
    font-size: 30px;
    letter-spacing: 1px;
  }
</style>
</head>
<body>
<main class="canvas">
  <section class="card card-front" aria-label="Card front">
    <div class="front-bar front-bar-left"></div>
    <div class="front-bar front-bar-right"></div>
    <h1 class="brand-name">BYTEHARBOR.ZONE</h1>
    <div class="rule"></div>
    <p class="contact-name">DANA WHITLOW</p>
    <p class="contact-phone">1-800-555-0147</p>
    <div class="rule"></div>
    <ul class="offer-list">
      <li>WE COME TO YOU</li>
      <li>ONLY $49/HR</li>
      <li>NO CONTRACT, NO MONTHLY FEE</li>
      <li>SOFTWARE ENGINEER ON STAFF</li>
      <li>REMOTE ASSISTANCE OR VISIT IN YOUR OFFICE</li>
    </ul>
  </section>

  <section class="card card-back" aria-label="Card back">
    <ul class="service-list">
      <li>SERVER SETUP</li>
      <li>NETWORK TROUBLESHOOTING</li>
      <li>PRINTER SETUP</li>
      <li>SECURE BACKUP SETUP</li>
      <li>SOFTWARE INSTALLATION</li>
      <li>WIRELESS NETWORK SETUP</li>
      <li>WIRED NETWORK SETUP</li>
      <li>WEBSITE MANAGEMENT</li>
      <li>ANY OTHER TECHNOLOGY RELATED SUPPORT</li>
      <li>EMAIL SETUP</li>
      <li>HIPAA COMPLIANCE REVIEW AND SETUP</li>
    </ul>
    <p class="service-extra">DISASTER RECOVERY</p>
    <p class="back-brand">BYTEHARBOR.ZONE</p>
  </section>
</main>
</body>
</html>
```